Rare Glow Edibles Gummies

Packaging design for custom mylars for cannabis infused gummies. I need a space for a warning label, nutrition facts, ingredients, brand logo and then individualized item details. We will later be doing assorted peanut butter cups, hard candies, etc.

```html
<!DOCTYPE html>
<html lang="en">
<head>
<meta charset="utf-8">
<title>Rare Glow Edibles – Blue Raspberry Gummies Mylar</title>
<link href="https://fonts.googleapis.com/css2?family=Montserrat:ital,wght@0,400;0,500;0,600;0,700;0,800;1,700;1,800&family=Kaushan+Script&family=Open+Sans:wght@400&display=swap" rel="stylesheet">
<style>
  :root {
    --page: #ffffff;
    --navy: #0a3275;
    --royal: #2f5aab;
    --sky: #4a80d4;
    --gummy-light: #3fa3c9;
    --gummy-dark: #12526e;
    --berry: #4a5fd8;
    --white: #ffffff;
    --ink: #111111;
  }
  * { box-sizing: border-box; margin: 0; padding: 0; }
  html, body {
    width: 1200px; height: 1000px; overflow: hidden;
    background: var(--page);
  }
  .stage { position: relative; width: 1200px; height: 1000px; }

  .panel {
    position: absolute; top: 265px; height: 466px; overflow: hidden;
    color: var(--white);
    font-family: "Montserrat", Arial, sans-serif;
  }
  .panel-front { left: 177px; width: 364px; }
  .panel-back  { left: 694px; width: 359px; }
  .panel-art { position: absolute; inset: 0; width: 100%; height: 100%; }

  /* brand mark */
  .brand { position: absolute; }
  .brand-ring {
    position: absolute; border: 2px solid var(--white); border-radius: 50%;
  }
  .brand-name {
    position: absolute; white-space: nowrap; text-align: center;
    font-family: "Montserrat", Arial, sans-serif; font-weight: 500;
    color: var(--white); line-height: 1;
  }
  .brand-name span { display: block; }
  .front-brand .brand-ring { left: 62px; top: 14px; width: 164px; height: 164px; }
  .front-brand .brand-name { left: 95px; top: 68px; width: 180px; }
  .front-brand .brand-word { font-size: 30px; }
  .front-brand .brand-sub { font-size: 14px; letter-spacing: 6px; margin-top: 8px; }

  .back-brand .brand-ring { left: 169px; top: 338px; width: 120px; height: 120px; }
  .back-brand .brand-name { left: 190px; top: 375px; width: 150px; }
  .back-brand .brand-word { font-size: 22px; }
  .back-brand .brand-sub { font-size: 10px; letter-spacing: 4.5px; margin-top: 6px; }

  /* front details */
  .flavor-art {
    position: absolute; left: 12px; top: 374px; width: 68px; height: 54px;
    border-radius: 50% 50% 45% 45%;
    background: radial-gradient(circle at 40% 55%, var(--berry), #2d3fb3 70%, rgba(47,90,171,0) 100%);
  }
  .flavor-name {
    position: absolute; left: 84px; top: 383px;
    font-family: "Kaushan Script", cursive; font-size: 23px; line-height: 1;
    text-shadow: 0 0 8px rgba(255,255,255,.55);
  }
  .potency {
    position: absolute; right: 20px; top: 444px;
    font-weight: 800; font-size: 8.6px; letter-spacing: 1.1px;
  }

  /* back details */
  .claims {
    position: absolute; left: 24px; top: 26px;
    font-weight: 700; font-style: italic; font-size: 12px; line-height: 16.6px;
    white-space: nowrap;
  }
  .notice { position: absolute; left: 24px; width: 140px; }
  .notice h2 { font-weight: 700; font-size: 15.5px; line-height: 1; margin-bottom: 3px; }
  .notice p { font-weight: 600; font-size: 9.6px; line-height: 12.4px; }
  .notice-warning { top: 121px; }
  .notice-dosing { top: 239px; }
  .ingredients {
    position: absolute; left: 24px; top: 392px;
    font-weight: 600; font-size: 9px; line-height: 12px; text-transform: uppercase;
  }

  .nutrition {
    position: absolute; left: 175px; top: 81px; width: 153px; height: 244px;
    border: 1.5px solid var(--white); padding: 2px 4px;
    font-size: 7.3px; line-height: 9.4px; font-weight: 500;
  }
  .nutrition h3 { font-weight: 800; font-size: 16.5px; line-height: 18px; letter-spacing: .2px; }
  .nf-row { display: flex; justify-content: space-between; border-top: 1px solid var(--white); }
  .nf-row.indent span:first-child { padding-left: 7px; }
  .nf-row.plain { border-top: none; }
  .nf-row b { font-weight: 700; }
  .nf-bar { height: 5px; background: var(--white); margin: 1px 0; }
  .nf-bar.mid { height: 3px; }
  .nf-serving { font-weight: 600; }
  .nf-calories {
    display: flex; justify-content: space-between; align-items: flex-end;
    font-weight: 800; font-size: 14px; line-height: 14px; padding-bottom: 2px;
  }
  .nf-calories .num { font-size: 19px; }
  .nf-dv { text-align: right; font-size: 6.4px; border-top: 2px solid var(--white); }
  .nf-foot { font-size: 4.6px; line-height: 5.6px; border-top: 2px solid var(--white); padding-top: 1px; }

  .note {
    position: absolute; left: 79px; top: 546px;
    font-family: "Open Sans", Arial, sans-serif; font-size: 13px; color: var(--ink);
  }
  .note-arrow { position: absolute; left: 0; top: 0; width: 1200px; height: 1000px; pointer-events: none; }
</style>
</head>
<body>
<main class="stage">

  <section class="panel panel-front">
    <svg class="panel-art" viewBox="0 0 637 816" preserveAspectRatio="none">
      <rect width="637" height="816" fill="var(--royal)"/>
      <path d="M0,395 C140,425 300,255 500,285 C570,295 610,300 637,305 L637,665 C580,610 520,540 420,630 C340,700 230,665 0,565 Z" fill="var(--sky)"/>
      <defs>
        <radialGradient id="gummyTone" cx="45%" cy="55%" r="65%">
          <stop offset="0" stop-color="var(--gummy-light)"/>
          <stop offset="1" stop-color="var(--gummy-dark)"/>
        </radialGradient>
      </defs>
      <path role="img" aria-label="Clear window showing sugared blue raspberry gummies"
            d="M90,400 C120,370 180,360 230,335 C320,300 430,280 555,287 L555,420 C545,440 540,410 532,430 L532,690 L512,690 L512,610 C480,650 400,660 330,645 C270,660 210,630 190,570 L135,575 L132,610 C128,630 108,630 104,610 L100,480 C78,470 74,440 80,420 Z"
            fill="url(#gummyTone)"/>
    </svg>

    <div class="brand front-brand">
      <div class="brand-ring"></div>
      <div class="brand-name"><span class="brand-word">Rare Glow</span><span class="brand-sub">EDIBLES</span></div>
    </div>

    <div class="flavor-art" role="img" aria-label="Blue raspberries with leaves"></div>
    <div class="flavor-name">Blue Raspberry Flavor</div>
    <div class="potency">20MG D8 PER PIECE</div>
  </section>

  <section class="panel panel-back">
    <svg class="panel-art" viewBox="0 0 628 816" preserveAspectRatio="none">
      <rect width="628" height="816" fill="var(--sky)"/>
      <path d="M0,0 H628 V140 C560,118 480,105 420,118 C300,142 200,200 90,190 C50,186 20,176 0,165 Z" fill="var(--navy)"/>
      <path d="M0,565 C100,610 170,650 235,628 C330,592 385,525 470,560 C540,590 600,640 628,660 V816 H0 Z" fill="var(--royal)"/>
    </svg>

    <p class="claims">LAB TESTED FOR QUALITY AND CONSISTENCY<br>INFUSED WITH SOLVENT FREE HEMP DISTILLATE</p>

    <div class="notice notice-warning">
      <h2>WARNING:</h2>
      <p>The intoxicating effects of this product maybe delayed up to two hours.May cause drowsiness. The product may impair the ability to drive or operate machinery. Please use extreme caution.</p>
    </div>
    <div class="notice notice-dosing">
      <h2>DOSING:</h2>
      <p>The appropriate dose may be different for each person. Please consult your physician.Consume with care.</p>
    </div>

    <div class="nutrition">
      <h3>Nutrition Facts</h3>
      <div class="nf-row nf-serving"><span>Serving size</span><b>1 Piece(3g)</b></div>
      <div class="nf-bar"></div>
      <div class="nf-row plain nf-serving"><span>Amount Per Serving</span></div>
      <div class="nf-calories"><span>Calories</span><span class="num">10</span></div>
      <div class="nf-dv">%Daily Value*</div>
      <div class="nf-row"><span>Total Fat 0g</span><b>0%</b></div>
      <div class="nf-row indent"><span>Saturated Fat 0g</span><b>0%</b></div>
      <div class="nf-row indent"><span><i>Trans Fat</i> 0g</span><span></span></div>
      <div class="nf-row"><span>Cholesterol 0g</span><b>0%</b></div>
      <div class="nf-row"><span>Sodium 0mg</span><b>0%</b></div>
      <div class="nf-row"><span>Total Carbhydrate 3g</span><b>1%</b></div>
      <div class="nf-row indent"><span>Dietary fiber 0g</span><b>0%</b></div>
      <div class="nf-row indent"><span>Total Sugars 2g</span><span></span></div>
      <div class="nf-row indent"><span>Includes 2g Added Sugars</span><b>4%</b></div>
      <div class="nf-row"><span>Protein 0g</span><span></span></div>
      <div class="nf-bar"></div>
      <div class="nf-row plain"><span>Vitamin D 0mcg</span><b>0%</b></div>
      <div class="nf-row"><span>Calcium 0mg</span><b>0%</b></div>
      <div class="nf-row"><span>Iron 0mg</span><b>0%</b></div>
      <div class="nf-row"><span>Potassium 0mg</span><b>0%</b></div>
      <div class="nf-foot">*The % Daily Value (DV) tells you how much a nutrient in a serving of food contributes to a daily diet. 2,000 calories a day is used for general nutrition advice.</div>
    </div>

    <p class="ingredients">Ingredients:<br>Sugar, Tapioca Syrup,<br>Water, Pectin, Citric<br>Acid, Hemp Extract</p>

    <div class="brand back-brand">
      <div class="brand-ring"></div>
      <div class="brand-name"><span class="brand-word">Rare Glow</span><span class="brand-sub">EDIBLES</span></div>
    </div>
  </section>

  <p class="note">transparent</p>
  <svg class="note-arrow" viewBox="0 0 1200 1000">
    <path d="M151,557 C190,566 215,572 238,556" fill="none" stroke="var(--ink)" stroke-width="2.2" stroke-linecap="round"/>
    <path d="M238,556 L259,538" fill="none" stroke="var(--ink)" stroke-width="2.2" stroke-linecap="round"/>
    <path d="M259,538 L248,541 L254,548 Z" fill="var(--ink)" stroke="var(--ink)" stroke-width="2" stroke-linejoin="round"/>
  </svg>

</main>
</body>
</html>
```